Clean professional business card design

Need a professional looking, high quality card and letterhead design. Business card would prefer to have a grey tone to the background.

Back of card needs to have: "Securities offered through Volmara Wealth Partners LLC (doing Insurance business in CA as VWPGS Insurance Agency), member OBREK/TADL. Advisory services offered through Volmara Asset Counsel LLC. Volmara entities are under separate ownership from any other named entity. [employee name] CA Insurance Lic #7K24903

Industry/Entity Type

Financial Planning

Font styles to use
Serif
Sans Serif

Requirements
Must have
• Customization of text so that I can adjust for other employee

```html
<!DOCTYPE html>
<html lang="en">
<head>
<meta charset="utf-8">
<title>Keystead Financial Advisers – Business Card</title>
<link rel="stylesheet" href="https://fonts.googleapis.com/css2?family=Open+Sans:wght@400;600;700&display=swap">
<style>
  :root {
    --page-bg: #dfe1e4;
    --card-bg: #f2f3f4;
    --brand-blue: #0b6fbf;
    --ink-dark: #2b2b2b;
    --ink-white: #ffffff;
  }
  * { margin: 0; padding: 0; box-sizing: border-box; }
  html, body {
    width: 1200px;
    height: 900px;
    overflow: hidden;
    background: var(--page-bg);
    font-family: "Open Sans", Arial, sans-serif;
  }
  .canvas {
    position: relative;
    width: 1200px;
    height: 900px;
  }
  .business-card {
    position: absolute;
    left: 180px;
    top: 191px;
    width: 840px;
    height: 518px;
    background: var(--card-bg);
    overflow: hidden;
    box-shadow: 0 10px 30px rgba(0,0,0,0.15);
  }
  .contact-band {
    position: absolute;
    left: 0;
    top: 0;
    width: 840px;
    height: 518px;
  }
  .person {
    position: absolute;
    right: 31px;
    top: 48px;
    text-align: right;
  }
  .person-name {
    font-size: 39px;
    font-weight: 600;
    color: var(--ink-dark);
    line-height: 1.1;
  }
  .person-name .first-name { color: var(--brand-blue); }
  .person-title {
    font-size: 25px;
    color: var(--ink-dark);
    margin-top: 2px;
  }
  .brand {
    position: absolute;
    left: 40px;
    top: 150px;
    display: flex;
    align-items: center;
    gap: 18px;
  }
  .brand-square {
    width: 54px;
    height: 54px;
    background: var(--brand-blue);
    flex: none;
  }
  .brand-name {
    font-size: 34px;
    font-weight: 600;
    color: var(--brand-blue);
    line-height: 1.15;
    width: 330px;
  }
  .license {
    position: absolute;
    right: 31px;
    top: 236px;
    font-size: 25px;
    font-weight: 700;
    color: var(--ink-dark);
  }
  .contact-list {
    position: absolute;
    right: 22px;
    top: 336px;
    list-style: none;
    text-align: right;
    color: var(--ink-white);
    font-size: 26px;
  }
  .contact-list li {
    display: flex;
    justify-content: flex-end;
    align-items: center;
    gap: 14px;
    height: 36px;
  }
  .contact-list svg { width: 20px; height: 20px; flex: none; }
  .address {
    position: absolute;
    right: 22px;
    top: 462px;
    font-size: 22px;
    color: var(--ink-white);
  }
</style>
</head>
<body>
<main class="canvas">
  <section class="business-card">
    <svg class="contact-band" viewBox="0 0 840 518" aria-hidden="true">
      <path d="M0 518 C 150 372, 440 292, 690 293 C 760 294, 810 302, 840 312 L 840 518 Z" fill="var(--brand-blue)"/>
    </svg>

    <div class="person">
      <p class="person-name"><span class="first-name">Daniel</span> Harlow</p>
      <p class="person-title">CA Insurance</p>
    </div>

    <div class="brand">
      <span class="brand-square"></span>
      <p class="brand-name">Keystead Financial Advisers</p>
    </div>

    <p class="license">LIC #7K24903</p>

    <ul class="contact-list">
      <li>555-014-2276
        <svg viewBox="0 0 20 20"><path d="M2 8 C 2 4, 18 4, 18 8 L 15 9 L 14 7 C 11 6, 9 6, 6 7 L 5 9 Z M5 10 H15 L16 16 H4 Z" fill="#fff"/><circle cx="10" cy="13" r="1.6" fill="var(--brand-blue)"/></svg>
      </li>
      <li>hello@keystead-mail.com
        <svg viewBox="0 0 20 20"><rect x="2" y="5" width="16" height="11" fill="#fff"/><path d="M2 5 L10 11 L18 5" fill="none" stroke="var(--brand-blue)" stroke-width="1.5"/></svg>
      </li>
      <li>www.keystead-fa.com
        <svg viewBox="0 0 20 20"><g fill="none" stroke="#fff" stroke-width="2.2" stroke-linecap="round"><path d="M9 7 L12 4 A3 3 0 0 1 16 8 L13 11"/><path d="M11 13 L8 16 A3 3 0 0 1 4 12 L7 9"/><path d="M8 12 L12 8"/></g></svg>
      </li>
    </ul>

    <p class="address">1234, Address Goes Here Country Name, 123456</p>
  </section>
</main>
</body>
</html>
```